Brindle Tides Boat Business Website

I would like a website that looks fresh, fun and exciting with great colors and photos of people having fun sailing and power boating. Current web page is www.brindletides.example. I want to be able to change content and photos myself once completed. Also needs to have customized info request forms and access to enrollment forms. Should work across all browsers and platforms including iPad and Mac. I have three product lines...instruction, charters and trips. See also keelhour.example/new-york, and facebook.com/brindletides, /keelhournewyork and /conchlagoonbar.
Updates

Reason: We are reviewing the designs submitted and will provide feedback asap. Thank you.

Industry/Entity Type

Business

Requirements
Must have
• self management/content management
form submissions
color, fun, excitement
links pages
photo pages
Nice to have
• calendar/class scheduling
guest book
visitor uploadable photos

```html
<!DOCTYPE html>
<html lang="en">
<head>
<meta charset="utf-8">
<title>Brindle Tides – Charter Co. &amp; Nautical School</title>
<link href="https://fonts.googleapis.com/css2?family=Cinzel:wght@400;700&family=Great+Vibes&family=Open+Sans:wght@300;400;600;700&display=swap" rel="stylesheet">
<style>
:root{
  --navy:#17466d;
  --blue:#1d5b88;
  --panel:rgba(26,84,128,.92);
  --teal:#3fae9a;
  --orange:#f2a21b;
  --gold:#d9a33a;
  --ink:#2b2b2b;
  --muted:#8d8d8d;
  --line:#e2e2e2;
  --page:#f4f4f4;
  --footer:#f0f0f0;
}
*{box-sizing:border-box;margin:0;padding:0}
html,body{width:678px;height:1200px;overflow:hidden}
body{position:relative;background:var(--page);font-family:"Open Sans",Arial,sans-serif;color:var(--ink)}
.abs{position:absolute}
.photo{position:absolute}

/* header */
.site-header{left:0;top:0;width:678px;height:60px;background:#fff}
.brand{left:82px;top:16px;display:flex;align-items:center;gap:6px}
.brand-dot{width:13px;height:13px;border-radius:50%;background:var(--teal)}
.brand-name{font-family:"Cinzel",serif;font-size:15px;color:var(--navy);font-weight:700;white-space:nowrap}
.brand-tag{left:82px;top:38px;font-family:"Cinzel",serif;font-size:6.5px;color:var(--navy);letter-spacing:.3px;white-space:nowrap}
.social-top{left:455px;top:6px;display:flex;gap:8px}
.social-top span{width:9px;height:9px;border-radius:50%;background:var(--navy);display:block}
.top-phone{left:515px;top:3px;font-family:"Cinzel",serif;font-size:12px;font-weight:400;color:#222;display:flex;align-items:center;gap:4px;white-space:nowrap}
.main-nav{left:234px;top:34px;display:flex;font-family:"Cinzel",serif;font-size:7.6px;color:#333;white-space:nowrap}
.main-nav a{color:inherit;text-decoration:none;padding:4px 5px;height:19px;line-height:10px}
.main-nav a.active{background:var(--navy);color:#fff;border:1px solid #0e3250}

/* hero */
.hero-photo{left:0;top:60px;width:678px;height:284px;background:linear-gradient(180deg,#9fc4dc 0%,#5f9cbf 35%,#6a8a87 60%,#8c7a62 100%)}
.signup{left:415px;top:72px;width:182px;height:262px;background:var(--panel);color:#fff;padding:0 14px}
.signup h2{font-family:"Great Vibes",cursive;font-weight:400;font-size:24px;text-align:center;margin-top:10px}
.dots{height:1px;border-top:1px dotted rgba(255,255,255,.7);margin:6px 0 6px;position:relative}
.dots::after{content:"";position:absolute;left:50%;top:-3px;width:4px;height:4px;border-radius:50%;background:#fff}
.signup label{display:block;font-size:7.5px;margin-top:4px}
.field{height:16px;background:#fff;margin-top:3px}
.row{display:flex;gap:6px}
.row>div{flex:1}
.select{position:relative}
.select::after{content:"";position:absolute;right:3px;top:6px;border:3px solid transparent;border-top-color:#666}
.zip{display:flex;align-items:center;gap:6px;font-size:5.5px}
.book{display:block;margin:12px auto 0;width:96px;height:24px;border-radius:12px;background:linear-gradient(#fbbf3a,#ee8d10);color:#fff;font-size:9px;font-weight:700;text-align:center;line-height:24px;border:1px solid #c97507}

/* welcome */
.welcome-photo{left:80px;top:365px;width:153px;height:88px;background:linear-gradient(180deg,#cfe3f1,#3c7aa8 60%,#1e4f79)}
.welcome-card{left:233px;top:370px;width:364px;height:78px;background:#fff;box-shadow:0 1px 3px rgba(0,0,0,.18);padding:6px 10px}
.welcome-card h1{font-family:"Cinzel",serif;font-weight:400;font-size:15.5px;color:var(--navy)}
.welcome-card h1 em{font-style:normal;color:var(--orange)}
.welcome-card p{font-size:6.4px;line-height:10px;color:var(--muted);margin-top:3px}
.welcome-card b{color:var(--blue);font-style:italic}

/* section heading */
.section-title{left:0;width:678px;text-align:center;font-family:"Cinzel",serif;font-weight:400;font-size:20px;color:var(--navy)}
.section-title em{font-style:normal;color:var(--orange)}
.band{left:80px;width:517px;height:5px;background:#e4e4e4}

/* guests */
.guest{width:86px;height:86px;border-radius:50%;background:#fff;box-shadow:0 2px 4px rgba(0,0,0,.25);padding:4px}
.guest i{display:block;width:100%;height:100%;border-radius:50%}
.guest.featured{border:4px solid var(--teal);padding:3px}
.arrow{width:17px;height:17px;border-radius:50%;display:flex;align-items:center;justify-content:center}
.slider-line{left:80px;top:675px;width:517px;height:1px;background:var(--gold)}
.slider-thumb{left:94px;top:672px;width:62px;height:7px;border-radius:4px;background:var(--teal)}

/* classes */
.class-photo{left:80px;width:123px;height:77px}
.class-title{left:210px;font-family:"Cinzel",serif;font-weight:400;font-size:12px;color:var(--navy);white-space:nowrap}
.class-text{left:210px;width:222px;font-size:6.3px;line-height:10px;color:var(--muted)}
.class-meta{left:210px;width:224px;height:15px;background:#fff;border:1px solid #ddd;font-size:5.6px;color:#555;display:flex;gap:16px;align-items:center;padding-left:6px}
.class-meta b{font-weight:400;color:#222}
.divider{left:80px;width:356px;height:2px;background:#ddd}
.pager{left:183px;top:992px;display:flex;gap:2px;font-size:5.5px}
.pager span{border:1px solid #999;background:#fff;padding:1px 3px;height:9px;line-height:6px}
.pager .gap{border:0;background:none;letter-spacing:1px}

.visitors{left:447px;top:772px;width:150px;height:233px;background:var(--navy);box-shadow:0 2px 4px rgba(0,0,0,.3)}
.visitors h3{font-family:"Cinzel",serif;font-weight:400;color:#fff;font-size:12px;margin:8px 0 0 7px}
.visitor-grid{left:6px;top:28px;width:139px;height:192px;background:linear-gradient(135deg,#c9a88a,#7a5f4d 50%,#d7c2b0)}

/* newsletter */
.newsletter{left:0;top:1047px;width:678px;height:38px;background:var(--blue);border-bottom:3px solid #0f3a5d;color:#fff}
.newsletter .label{left:80px;top:10px;font-size:12.5px;font-weight:300;white-space:nowrap}
.newsletter .input{left:236px;top:8px;width:155px;height:22px;background:#fff}
.newsletter .follow{left:438px;top:12px;font-size:12.5px;font-weight:300;white-space:nowrap}
.ring{width:20px;height:20px;border-radius:50%;border:2px solid #fff}

/* footer */
.site-footer{left:0;top:1088px;width:678px;height:112px;background:var(--footer)}
.fcol{top:12px}
.fcol h4{font-size:7.5px;font-weight:700;color:#333;padding-bottom:4px;border-bottom:1px solid #ccc;width:90px}
.fcol ul{list-style:none;margin-top:5px}
.fcol li{font-size:5.6px;color:#444;line-height:10.3px}
.fcol li::before{content:"» ";color:#c33}
.contact-phone{font-size:9px;color:#444;display:flex;gap:4px;align-items:center;margin-top:6px}
.contact-addr{font-size:5.3px;line-height:8px;color:#444;margin-top:3px;padding-left:12px;position:relative}
.contact-mail{font-size:6px;color:#444;margin-top:4px;display:flex;gap:4px;align-items:center}
</style>
</head>
<body>

<header class="site-header abs">
  <div class="brand abs"><span class="brand-dot"></span><span class="brand-name">Brindle Tides</span></div>
  <div class="brand-tag abs">Charter Co. &amp; Nautical School</div>
  <div class="social-top abs"><span></span><span></span><span></span></div>
  <div class="top-phone abs">
    <svg width="9" height="9" viewBox="0 0 24 24"><path fill="#222" d="M6.6 10.8a15 15 0 0 0 6.6 6.6l2.2-2.2c.3-.3.7-.4 1-.2 1.1.4 2.300.6 3.6.6.6 0 1 .4 1 1V20c0 .6-.4 1-1 1A17 17 0 0 1 3 4c0-.6.4-1 1-1h3.5c.6 0 1 .4 1 1 0 1.3.2 2.5.6 3.6.1.3 0 .7-.2 1z"/></svg>
    1800-555-0142
  </div>
  <nav class="main-nav abs">
    <a class="active" href="#">Nautical School</a>
    <a href="#">Charter Sailing</a>
    <a href="#">Charter Power</a>
    <a href="#">Our Captains</a>
    <a href="#">Contact Us!</a>
  </nav>
</header>

<div class="hero-photo photo" role="img" aria-label="Group of smiling sailors in white shirts holding a club pennant on a wooden dock by the harbour"></div>

<form class="signup abs">
  <h2>Sign Up Today!</h2>
  <div class="dots"></div>
  <label>Name</label><div class="field"></div>
  <label>Address</label><div class="field"></div>
  <div class="row">
    <div><label>State</label><div class="field"></div></div>
    <div><label>City</label><div class="field select"></div></div>
  </div>
  <label>Zip Code:</label>
  <div class="zip"><div class="field" style="width:74px"></div><span>( 6 Digits )</span></div>
  <div class="dots" style="margin-top:10px"></div>
  <span class="book">BOOK NOW ›</span>
</form>

<div class="welcome-photo photo" role="img" aria-label="White motor yacht cruising on open water"></div>
<section class="welcome-card abs">
  <h1>Welcome to <em>Brindle Tides</em></h1>
  <p>We operate <b>KeelHour New York</b> (www.keelhour.example/new-york) the world's largest fractional boating company with bases in the US, Europe and Australia offering seasonal memberships on sail and power boats from 25' through 50'. We take the hassle and cost out of boating by providing access to a professionally maintained fleet that you can schedule through an on-line calendar. All you have to do is show up and go!</p>
</section>

<h2 class="section-title abs" style="top:487px">Our <em>guest's</em></h2>
<div class="band abs" style="top:519px"></div>

<div class="arrow abs" style="left:69px;top:596px;background:#bbb"><svg width="7" height="7" viewBox="0 0 10 10"><path d="M7 1 3 5l4 4" stroke="#fff" stroke-width="2" fill="none"/></svg></div>
<div class="guest abs" style="left:101px;top:560px"><i role="img" aria-label="Guest portrait" style="background:linear-gradient(#9aa7b4,#4b5968)"></i></div>
<div class="guest featured abs" style="left:230px;top:549px"><i role="img" aria-label="Featured guest portrait" style="background:linear-gradient(#b8c6d4,#2d3e57)"></i></div>
<div class="guest abs" style="left:360px;top:560px"><i role="img" aria-label="Guest portrait" style="background:linear-gradient(#e2e2e2,#7d7d7d)"></i></div>
<div class="guest abs" style="left:490px;top:560px"><i role="img" aria-label="Guest portrait" style="background:linear-gradient(#7f8a6a,#3a3a2f)"></i></div>
<div class="arrow abs" style="left:591px;top:596px;background:#666"><svg width="7" height="7" viewBox="0 0 10 10"><path d="M3 1l4 4-4 4" stroke="#fff" stroke-width="2" fill="none"/></svg></div>
<div class="slider-line abs"></div>
<div class="slider-thumb abs"></div>

<h2 class="section-title abs" style="top:716px">Calendar <em>/class scheduling</em></h2>
<div class="band abs" style="top:748px"></div>

<div class="class-photo photo" style="top:773px;background:linear-gradient(180deg,#c7dcec,#3a77a7 55%,#1d4b74)" role="img" aria-label="Motor yacht on the water"></div>
<h3 class="class-title abs" style="top:770px">There are majority have suffred.</h3>
<p class="class-text abs" style="top:788px">Lorem Ipsum is that it has making it look like readable English. Many desktop publishing packages and web page Lorem Ipsum as their default model and their infancy. that it has making it look like readable English. Many desktop publishing packages.</p>
<div class="class-meta abs" style="top:834px"><span>Day : <b>Sunday-Sunday</b></span><span>Time : <b>7:00-7:00 pm</b></span><span>Instructor : <b>Maren Holt</b></span></div>
<div class="divider abs" style="top:865px"></div>

<div class="class-photo photo" style="top:882px;background:linear-gradient(180deg,#d4dde3,#8a9aa6 50%,#3f4a52)" role="img" aria-label="Sailing students posing at a marina"></div>
<h3 class="class-title abs" style="top:879px">Lorem Ipsum is that it has making</h3>
<p class="class-text abs" style="top:897px">Lorem Ipsum is that it has making it look like readable English. Many desktop publishing packages and web page Lorem Ipsum as their default model and their infancy. that it has making it look like readable English. Many desktop publishing packages.</p>
<div class="class-meta abs" style="top:942px"><span>Day : <b>Sunday-Sunday</b></span><span>Time : <b>7:00-7:00 pm</b></span><span>Instructor : <b>Maren Holt</b></span></div>
<div class="divider abs" style="top:983px"></div>

<div class="pager abs"><span>&lt; Prev</span><span>1</span><span>2</span><span>3</span><span>4</span><span class="gap">..........</span><span>9</span><span>Next &gt;</span></div>
<div class="divider abs" style="top:1008px"></div>

<aside class="visitors abs">
  <h3>Visitors</h3>
  <div class="visitor-grid photo" role="img" aria-label="Grid of visitor profile photos"></div>
</aside>

<section class="newsletter abs">
  <span class="label abs">Subscribe Our Newsletter</span>
  <div class="input abs"></div>
  <span class="follow abs">Follow Us Here</span>
  <div class="ring abs" style="left:533px;top:9px"></div>
  <div class="ring abs" style="left:556px;top:9px"></div>
  <div class="ring abs" style="left:579px;top:9px"></div>
</section>

<footer class="site-footer abs">
  <div class="fcol abs" style="left:80px"><h4>INFORMATION</h4><ul><li>About Us</li><li>Delivery Information</li><li>Privacy Policy</li><li>Terms &amp; Conditions</li></ul></div>
  <div class="fcol abs" style="left:205px"><h4 style="width:104px">CUSTOMER SERVICE</h4><ul><li>Contact Us</li><li>Returns</li><li>Site Map</li></ul></div>
  <div class="fcol abs" style="left:352px"><h4>EXTRAS</h4><ul><li>Brands</li><li>Gift Vouchers</li><li>Affiliates</li><li>Specials</li></ul></div>
  <div class="fcol abs" style="left:482px">
    <h4 style="width:115px">CONTACT US</h4>
    <div class="contact-phone"><svg width="8" height="8" viewBox="0 0 24 24"><path fill="#444" d="M6.6 10.8a15 15 0 0 0 6.6 6.6l2.2-2.2c.3-.3.7-.4 1-.2 1.1.4 2.3.6 3.6.6.6 0 1 .4 1 1V20c0 .6-.4 1-1 1A17 17 0 0 1 3 4c0-.6.4-1 1-1h3.5c.6 0 1 .4 1 1 0 1.3.2 2.5.6 3.6.1.3 0 .7-.2 1z"/></svg>1800-555-0178</div>
    <div class="contact-addr"><svg width="6" height="8" viewBox="0 0 12 16" style="position:absolute;left:0;top:0"><path fill="#444" d="M6 0a6 6 0 0 0-6 6c0 4.5 6 10 6 10s6-5.5 6-10a6 6 0 0 0-6-6zm0 8.5A2.5 2.5 0 1 1 6 3.5a2.5 2.5 0 0 1 0 5z"/></svg>HARBOR STORE,<br>12, Quay Street, Dock Road,<br>Old Port 4410, Mast Tower<br>Pier Road, 22QT</div>
    <div class="contact-mail"><svg width="7" height="6" viewBox="0 0 14 12"><path fill="#444" d="M7 0 0 5v7h14V5z"/></svg>info@brindletides.example</div>
  </div>
</footer>

</body>
</html>
```